Business cards and stationary design

We just completed the design of our new logo and we need to print new business cards and letterhead for our nonprofit. We are looking for a fresh new design that shows off our new logo. On letterhead, we must have a column on the right or left to include our Board of Directors (up to 45 names) (see attachment)

Industry/Entity Type

Non-Profit

Contact Information for Business Card

Standard business card with name, title, Company name, mailing address phone numbers, email address and website. Tagline on back "Every Neighbor Deserves a Door"

Font styles to use
Sans Serif

Requirements
Must have
• include pertinent information above
• new logo
• fonts compatible with logo
• should use logo colors only
Nice to have
• tag lines

```html
<!DOCTYPE html>
<html lang="en">
<head>
<meta charset="utf-8">
<title>Hearthway Center – Business Card</title>
<link rel="stylesheet" href="https://fonts.googleapis.com/css2?family=Open+Sans:wght@400;600;700&family=Lora:ital@1&display=swap">
<style>
  :root {
    --teal: #1f8ea3;
    --paper: #f4f5f4;
    --ink: #2a2f33;
    --white: #ffffff;
    --stage: #e7e4df;
    --photo-light: #c9c9c9;
    --photo-dark: #4a4a4a;
  }
  * { box-sizing: border-box; margin: 0; padding: 0; }
  html, body { width: 1200px; height: 1000px; overflow: hidden; }
  body {
    background: var(--stage);
    font-family: "Open Sans", Arial, sans-serif;
    position: relative;
  }
  .card {
    position: absolute;
    left: 240px;
    width: 720px;
    height: 411px;
    overflow: hidden;
    border-radius: 3px;
    box-shadow: 0 6px 18px rgba(0,0,0,0.15);
  }
  .card--front { top: 60px; background: var(--paper); }
  .card--back { top: 525px; background: var(--white); }

  .card__shape { position: absolute; inset: 0; width: 100%; height: 100%; }

  .holder { position: absolute; left: 88px; top: 52px; }
  .holder__name {
    color: var(--teal);
    font-weight: 700;
    font-size: 25px;
    letter-spacing: 1px;
  }
  .holder__title { color: var(--ink); font-size: 17px; font-weight: 600; margin-top: 2px; }

  .contacts {
    position: absolute; left: 88px; top: 150px;
    list-style: none;
  }
  .contacts__item {
    display: flex; align-items: flex-start; gap: 14px;
    color: var(--ink); font-size: 15px; line-height: 1.2;
    height: 44px;
  }
  .contacts__icon { width: 22px; height: 22px; flex: none; }

  .brand {
    position: absolute;
    color: var(--white);
    font-weight: 600;
    letter-spacing: 2px;
    text-transform: uppercase;
    display: flex; align-items: center; gap: 10px;
    white-space: nowrap;
  }
  .brand__dot { width: 14px; height: 14px; border-radius: 50%; background: var(--white); }
  .card--front .brand { right: 40px; top: 300px; font-size: 19px; }
  .card--back .brand { left: 40px; top: 185px; font-size: 19px; }

  .tagline {
    position: absolute; left: 64px; top: 222px;
    color: var(--white);
    font-family: "Lora", Georgia, serif;
    font-style: italic;
    font-size: 17px;
    white-space: nowrap;
  }

  .photo-area {
    position: absolute; inset: 0;
    background: radial-gradient(ellipse at 62% 55%, var(--photo-dark) 0%, #7a7a7a 45%, var(--photo-light) 100%);
  }
</style>
</head>
<body>

  <section class="card card--front" aria-label="Business card front">
    <svg class="card__shape" viewBox="0 0 720 411" preserveAspectRatio="none" aria-hidden="true">
      <polygon points="265,411 720,411 720,42" fill="var(--teal)"/>
    </svg>

    <header class="holder">
      <h1 class="holder__name">DANA WHITFIELD</h1>
      <p class="holder__title">Director</p>
    </header>

    <ul class="contacts">
      <li class="contacts__item">
        <svg class="contacts__icon" viewBox="0 0 22 22" aria-hidden="true">
          <circle cx="11" cy="11" r="11" fill="var(--teal)"/>
          <path d="M11 5a4 4 0 0 0-4 4c0 3 4 8 4 8s4-5 4-8a4 4 0 0 0-4-4z" fill="var(--white)"/>
          <circle cx="11" cy="9" r="1.5" fill="var(--teal)"/>
        </svg>
        <span>1872 Calder Avenue, Dallas TX<br>75204</span>
      </li>
      <li class="contacts__item">
        <svg class="contacts__icon" viewBox="0 0 22 22" aria-hidden="true">
          <circle cx="11" cy="11" r="11" fill="var(--teal)"/>
          <path d="M7.5 6.5l2 0 1 2.5-1.3 1a6 6 0 0 0 3 3l1-1.3 2.5 1v2a1 1 0 0 1-1 1A8.5 8.5 0 0 1 6.5 7.5a1 1 0 0 1 1-1z" fill="var(--white)"/>
        </svg>
        <span>214 555 0187</span>
      </li>
      <li class="contacts__item">
        <svg class="contacts__icon" viewBox="0 0 22 22" aria-hidden="true">
          <circle cx="11" cy="11" r="11" fill="var(--teal)"/>
          <rect x="6" y="7.5" width="10" height="7" fill="none" stroke="var(--white)" stroke-width="1.4"/>
          <path d="M6 7.5l5 4 5-4" fill="none" stroke="var(--white)" stroke-width="1.4"/>
        </svg>
        <span>info@hearthwaycenter.org</span>
      </li>
      <li class="contacts__item">
        <svg class="contacts__icon" viewBox="0 0 22 22" aria-hidden="true">
          <circle cx="11" cy="11" r="11" fill="var(--teal)"/>
          <path d="M11 5.5l-5.5 5h1.5v5h3v-3h2v3h3v-5h1.5z" fill="var(--white)"/>
        </svg>
        <span>www.hearthwaycenter.org</span>
      </li>
    </ul>

    <div class="brand"><span class="brand__dot"></span>Hearthway Center</div>
  </section>

  <section class="card card--back" aria-label="Business card back">
    <div class="photo-area" role="img" aria-label="Black and white photograph of an elderly man in a knit cap and jacket, seated outdoors"></div>
    <svg class="card__shape" viewBox="0 0 720 411" preserveAspectRatio="none" aria-hidden="true">
      <polygon points="0,0 216,0 418,411 0,411" fill="var(--teal)"/>
    </svg>
    <div class="brand"><span class="brand__dot"></span>Hearthway Center</div>
    <p class="tagline">Every Neighbor Deserves a Door</p>
  </section>

</body>
</html>
```